Cover for Where the Quiet River Bends Beyond Our Morning

Cover for a book that describes everything that happens to a person, from pre-birth life plans through growing in compassion and wisdom to death and living in the afterlife. The information is revealed in messages from people living in the life after this life. The title is Lanterns Along the Hidden Stair of Every Soul: Gathered from Voices Dwelling in the Further Meadow. Author is T. Morven Ashdale. Book size is 6 by 9.

Target Market(s)

General

Font styles to use
Serif

```html
<!DOCTYPE html>
<html lang="en">
<head>
<meta charset="utf-8">
<title>Lanterns Along the Hidden Stair of Every Soul — Cover</title>
<link href="https://fonts.googleapis.com/css2?family=Josefin+Sans:wght@400;600&family=Playfair+Display:wght@900&family=Cinzel:wght@600&display=swap" rel="stylesheet">
<style>
  :root {
    --ink-dark: #1a0c06;
    --ember: #e8701e;
    --flame: #f7a648;
    --glow: #ffd89a;
    --ash: #3b2a22;
    --water: #5c6068;
    --title-white: #fbf4ea;
    --title-gold: #f4b93a;
    --title-edge: #2a1407;
  }
  * { margin: 0; padding: 0; box-sizing: border-box; }
  html, body { width: 882px; height: 1200px; overflow: hidden; background: #ffffff; }
  .cover {
    position: relative;
    width: 882px;
    height: 1200px;
    overflow: hidden;
    background: var(--ink-dark);
  }
  .cover-art {
    position: absolute;
    inset: 0;
    background:
      radial-gradient(ellipse 32% 55% at 68% 48%, rgba(255,248,235,0.55), rgba(255,248,235,0) 70%),
      radial-gradient(ellipse 70% 45% at 55% 38%, var(--glow) 0%, var(--flame) 28%, var(--ember) 52%, rgba(232,112,30,0) 80%),
      linear-gradient(180deg, #2c130a 0%, #8a3a12 22%, #c4581a 42%, #7a3414 66%, var(--ash) 80%, var(--water) 92%, #2a2c30 100%);
  }
  .cover-vignette {
    position: absolute;
    inset: 0;
    background: radial-gradient(ellipse 90% 80% at 55% 45%, rgba(0,0,0,0) 55%, rgba(0,0,0,0.55) 100%);
  }
  .title {
    position: absolute;
    left: 52px;
    top: 120px;
    width: 560px;
    display: flex;
    flex-direction: column;
  }
  .title-light {
    font-family: "Josefin Sans", sans-serif;
    font-weight: 600;
    font-size: 56px;
    line-height: 1.12;
    letter-spacing: 1px;
    text-transform: uppercase;
    color: var(--title-white);
    text-shadow: 2px 2px 3px rgba(0,0,0,0.7);
  }
  .title-bold {
    font-family: "Playfair Display", serif;
    font-weight: 900;
    font-size: 78px;
    line-height: 1.05;
    text-transform: uppercase;
    color: var(--title-gold);
    -webkit-text-stroke: 2px var(--title-edge);
    text-shadow: 3px 3px 4px rgba(0,0,0,0.6);
  }
  .title-light.after-bold { margin-top: 8px; }
  .author {
    position: absolute;
    left: 52px;
    bottom: 48px;
    font-family: "Cinzel", serif;
    font-weight: 600;
    font-size: 50px;
    letter-spacing: 6px;
    text-transform: uppercase;
    color: var(--title-white);
    text-shadow: 2px 2px 4px rgba(0,0,0,0.8);
    white-space: nowrap;
  }
</style>
</head>
<body>
  <main class="cover">
    <div class="cover-art" role="img" aria-label="Fiery orange sky with a faint clock face and lightning, a woman in a flowing white dress reaching upward, standing in misty water"></div>
    <div class="cover-vignette"></div>

    <h1 class="title">
      <span class="title-light">Lanterns</span>
      <span class="title-light">Along</span>
      <span class="title-light">the Hidden</span>
      <span class="title-light">Stair of</span>
      <span class="title-light">Every Soul:</span>
      <span class="title-bold">Gathered</span>
      <span class="title-bold">from</span>
      <span class="title-bold">Voices</span>
      <span class="title-light after-bold">Dwelling in the</span>
      <span class="title-light">Further Meadow</span>
    </h1>

    <p class="author">T. Morven Ashdale</p>
  </main>
</body>
</html>
```